Larkmoor Blind Company / Blind Sale postcard mailer

I need a Design for a two sided postcard, advertising products for our company. One side will mainly show blinds & shutters, and the "call out" will be "Blind Sale / $59.99 per window". Then a place underneath for details. The other side of the card can showcase our other products (shades, exterior, etc). I would like the overall look and feel of the card to resemble the website design and colors, etc, you see at www.quillstonehome.example and www.fernwickdecor.example. You can use any images from my Stashbin page here: https://www.stashbin.example/sh/4kdmq8rtzvewplx/QQT2HHjbWpaLm731gxJtRsZ?dl=0

Use images from the Birchwave folder in Stashbin.
Also, my website for reference is www.larkmoorblinds.example
Larkmoor Blind Company

The printed card will be very plastic, heavy glossy. Heavier than most. I want the card to be as striking as possible, harder for customer to throw away. Trying to avoid lots of clutter on the card. Custom Template attached.

Target Market(s)

Card will be targeted mainly to new homeowners, especially new construction homes

Industry/Entity Type

It Company

Font styles to use
Serif
Sans Serif

Requirements
Must have
• Clean, uncluttered look. Best looking images. Logo somewhere on card. Open to changing the color of logo (i.e., if whites and greys are the main color, could do a white and grey version of logo..)

```html
<!DOCTYPE html>
<html lang="en">
<head>
<meta charset="utf-8">
<title>Larkmoor Blind Company – Blind Sale Postcard</title>
<link rel="stylesheet" href="https://fonts.googleapis.com/css2?family=Marcellus&family=Open+Sans:wght@500&display=swap">
<style>
  :root {
    --page-bg: #ecebe8;
    --ink-white: #ffffff;
    --ink-soft: #ece8ee;
    --wood-deep: #2a130c;
    --wood-mid: #5a2a18;
    --wood-warm: #7a3d22;
    --lamp-glow: #c98a4a;
    --shade-dark: #1a0d08;
  }
  * { box-sizing: border-box; margin: 0; padding: 0; }
  html, body {
    width: 1200px; height: 1000px; overflow: hidden;
    background: var(--page-bg);
  }
  .postcard {
    position: absolute;
    left: 67px; top: 241px;
    width: 1069px; height: 522px;
    overflow: hidden;
    color: var(--ink-white);
  }
  .hero-photo {
    position: absolute; inset: 0;
    background:
      radial-gradient(ellipse 220px 180px at 190px 190px, rgba(201,138,74,.75), transparent 70%),
      radial-gradient(ellipse 160px 140px at 810px 110px, rgba(201,138,74,.45), transparent 70%),
      linear-gradient(180deg, var(--wood-mid) 0%, var(--wood-warm) 40%, var(--wood-deep) 75%, var(--shade-dark) 100%);
  }
  .brand-box {
    position: absolute;
    left: 104px; top: 74px;
    width: 264px; height: 203px;
    border: 2px solid var(--ink-white);
    display: flex; flex-direction: column; justify-content: center; align-items: center;
    font-family: "Open Sans", sans-serif; font-weight: 500;
    font-size: 37px; line-height: 1.5; letter-spacing: 2px;
    text-align: center;
  }
  .sale-headline {
    position: absolute;
    left: 408px; top: 88px;
    font-family: "Marcellus", serif;
    font-size: 98px; letter-spacing: 15px; line-height: 1;
    color: var(--ink-soft);
    white-space: nowrap;
  }
  .sale-price {
    position: absolute;
    left: 411px; top: 188px;
    font-family: "Marcellus", serif;
    font-size: 57px; line-height: 1; letter-spacing: 0.5px;
    color: var(--ink-soft);
    white-space: nowrap;
  }
  .product-row {
    position: absolute;
    left: 28px; top: 319px;
    display: flex; gap: 5px;
  }
  .product { width: 250px; text-align: center; }
  .product-photo {
    height: 92px;
    border: 1.5px solid var(--ink-white);
  }
  .photo-shutters { background: linear-gradient(90deg, #6b4a2c, #d9cdb0 30%, #8a6a44 55%, #e2d6bc 80%, #6b4a2c); }
  .photo-shades   { background: linear-gradient(90deg, #e9ecee, #f7f8f8 40%, #c9ccce 70%, #f3f3f1); }
  .photo-blinds   { background: linear-gradient(90deg, #4a2614, #8a4a24 35%, #e8e2d2 55%, #7a3e1e 80%, #4a2614); }
  .photo-exterior { background: linear-gradient(90deg, #3a1218, #d8dce0 30%, #a45a5a 60%, #e6e6e2 85%, #888a86); }
  .product-label {
    margin-top: 14px;
    font-family: "Marcellus", serif;
    font-size: 30px; letter-spacing: 1px; line-height: 1;
  }
  .contact-line {
    position: absolute;
    left: 0; right: 6px; top: 480px;
    text-align: center;
    font-family: "Marcellus", serif;
    font-size: 17px; letter-spacing: 0.6px;
    white-space: nowrap;
  }
</style>
</head>
<body>
  <section class="postcard">
    <div class="hero-photo" role="img" aria-label="Warm wood-panelled living room with dark plantation shutters, glowing table lamps, a classical bust and a sofa"></div>

    <div class="brand-box">
      <span>LARKMOOR</span>
      <span>BLIND</span>
      <span>COMPANY</span>
    </div>

    <h1 class="sale-headline">BLIND SALE</h1>
    <p class="sale-price">$59.99 PER WINDOW</p>

    <div class="product-row">
      <div class="product">
        <div class="product-photo photo-shutters" role="img" aria-label="Dining room with white plantation shutters"></div>
        <p class="product-label">SHUTTERS</p>
      </div>
      <div class="product">
        <div class="product-photo photo-shades" role="img" aria-label="Bright white kitchen with window shades"></div>
        <p class="product-label">SHADES</p>
      </div>
      <div class="product">
        <div class="product-photo photo-blinds" role="img" aria-label="Sitting room with wooden blinds"></div>
        <p class="product-label">BLINDS</p>
      </div>
      <div class="product">
        <div class="product-photo photo-exterior" role="img" aria-label="Exterior window with shutters, flower box and wall lantern"></div>
        <p class="product-label">EXTERIOR</p>
      </div>
    </div>

    <p class="contact-line">TELEPHONE: 404-555-0148 &nbsp;FAX:815-555-0172 EMAIL: INFO@LARKMOORBLINDS.EXAMPLE</p>
  </section>
</body>
</html>
```